**** Business card design for VoltaNode ****

For my ICT company VoltaNode I need I need a business card design.

We design, build and host web-applications and we have our own CMS product.

Some good examples are attached.

The information should be:
Joris Tielenburg
Managing director
E: j.tielenburg@voltanode-example.nl
M: +31(0)6 57218064
T: +31(0)40 7249305
W: www.voltanode-example.nl

Address:
Berend Vlootweg 27
5612 KT Eindhoven

Industry/Entity Type

Business

Requirements
Must have
• - Use logo (see attachments)
- Double sided
- Distinctive
Nice to have
• - Place for a statement on the back-side: "Designed with knowledge, built with passion"
- HTML code (or Wordpress)
- Dark (black or dark-gray) side
- Small simple images for telephone, e-mail en Url.
- QR code (only if not disturbing), not required, just an option

```html
<!DOCTYPE html>
<html lang="en">
<head>
<meta charset="utf-8">
<title>VoltaNode business card</title>
<link rel="stylesheet" href="https://fonts.googleapis.com/css2?family=Cabin:wght@400;600&display=swap">
<style>
  :root {
    --backdrop: #d6d6d4;
    --card-white: #f7f7f5;
    --card-black: #050608;
    --glow: #123a78;
    --brand-blue: #2b7fc8;
    --mark-blue: #3a8fd6;
    --logo-grey: #6f7a86;
    --logo-light: #9fb4c8;
    --ink: #22262b;
    --rule: #b9bcc0;
    --band-navy: #1b2f78;
    --band-cyan: #6fd0e0;
  }
  * { box-sizing: border-box; margin: 0; padding: 0; }
  html, body { width: 1200px; height: 900px; overflow: hidden; }
  body {
    background: var(--backdrop);
    font-family: "Cabin", sans-serif;
    position: relative;
  }
  .card {
    position: absolute;
    left: 290px;
    width: 620px;
    height: 354px;
    overflow: hidden;
    box-shadow: 0 6px 18px rgba(0,0,0,0.18);
  }
  .card-back {
    top: 70px;
    background:
      radial-gradient(circle at 36% 44%, var(--glow) 0%, rgba(18,58,120,0.35) 18%, rgba(5,6,8,0) 40%),
      var(--card-black);
  }
  .card-front { top: 476px; background: var(--card-white); }

  .brand {
    position: absolute;
    display: flex;
    align-items: center;
    gap: 14px;
  }
  .brand-dot { border-radius: 50%; background: var(--mark-blue); flex: none; }
  .brand-name { font-weight: 400; letter-spacing: 0.5px; }

  .card-back .brand { left: 170px; top: 140px; }
  .card-back .brand-dot { width: 62px; height: 62px; }
  .card-back .brand-name { font-size: 40px; color: var(--logo-light); }

  .card-front .brand { left: 40px; top: 102px; }
  .card-front .brand-dot { width: 50px; height: 50px; }
  .card-front .brand-name { font-size: 31px; color: var(--logo-grey); }

  .divider {
    position: absolute;
    left: 322px; top: 30px;
    width: 1px; height: 218px;
    background: var(--rule);
  }
  .contact { position: absolute; left: 340px; top: 30px; color: var(--ink); }
  .contact-name { font-size: 17px; font-weight: 600; color: var(--brand-blue); letter-spacing: 0.3px; }
  .contact-role { font-size: 13px; margin-top: 1px; }
  .contact-list { list-style: none; font-size: 13px; line-height: 17px; }
  .contact-list.address { margin-top: 36px; }
  .contact-list.lines { margin-top: 18px; }
  .contact-list li { display: flex; align-items: flex-start; gap: 7px; }
  .contact-list .icon { width: 11px; height: 11px; flex: none; margin-top: 3px; fill: var(--brand-blue); }

  .band-line {
    position: absolute; left: 0; width: 100%;
    background: linear-gradient(90deg, var(--band-navy), var(--band-cyan));
  }
  .band-line.thin-top { top: 266px; height: 2px; }
  .band-line.thin-mid { top: 272px; height: 1px; }
  .band-line.main { top: 280px; height: 24px; }
</style>
</head>
<body>

<section class="card card-back" aria-label="Card back">
  <div class="brand">
    <span class="brand-dot"></span>
    <span class="brand-name">VoltaNode</span>
  </div>
</section>

<section class="card card-front" aria-label="Card front">
  <div class="brand">
    <span class="brand-dot"></span>
    <span class="brand-name">VoltaNode</span>
  </div>

  <div class="divider"></div>

  <div class="contact">
    <p class="contact-name">Joris Tielenburg</p>
    <p class="contact-role">Managing director</p>

    <ul class="contact-list address">
      <li>
        <svg class="icon" viewBox="0 0 12 12" aria-hidden="true"><path d="M6 0.5 0.5 5.5H2V11.5H5V8H7V11.5H10V5.5H11.5Z"/></svg>
        <span>Berend Vlootweg 27<br>5612 KT Eindhoven</span>
      </li>
    </ul>

    <ul class="contact-list lines">
      <li>
        <svg class="icon" viewBox="0 0 12 12" aria-hidden="true"><path d="M3 0H9V12H3ZM4 1.5V9.5H8V1.5Z"/></svg>
        <span>+31(0)6 57218064</span>
      </li>
      <li>
        <svg class="icon" viewBox="0 0 12 12" aria-hidden="true"><path d="M0.5 4C2 1.5 10 1.5 11.5 4L10 5.5 8.5 4.5V3.5H3.5V4.5L2 5.5ZM2.5 6.5H9.5L10.5 11H1.5Z"/></svg>
        <span>+31(0)40 7249305</span>
      </li>
      <li>
        <svg class="icon" viewBox="0 0 12 12" aria-hidden="true"><path d="M0.5 2.5H11.5V9.5H0.5ZM1.5 3.3 6 6.6 10.5 3.3Z"/></svg>
        <span>j.tielenburg@voltanode-example.nl</span>
      </li>
      <li>
        <svg class="icon" viewBox="0 0 12 12" aria-hidden="true"><path d="M6 0.5A5.5 5.5 0 1 0 6 11.5 5.5 5.5 0 1 0 6 0.5ZM1.8 5.3H4Q4.1 3 5.2 1.6 2.3 2.2 1.8 5.3ZM5 5.3H7Q6.9 3 6 1.7 5.1 3 5 5.3ZM8 5.3H10.2Q9.7 2.2 6.8 1.6 7.9 3 8 5.3ZM1.8 6.7Q2.3 9.8 5.2 10.4 4.1 9 4 6.7ZM5 6.7Q5.1 9 6 10.3 6.9 9 7 6.7ZM8 6.7Q7.9 9 6.8 10.4 9.7 9.8 10.2 6.7Z"/></svg>
        <span>www.voltanode-example.nl</span>
      </li>
    </ul>
  </div>

  <div class="band-line thin-top"></div>
  <div class="band-line thin-mid"></div>
  <div class="band-line main"></div>
</section>

</body>
</html>
```